Law Office needs stationery design and business card

I currently have been using the same letterhead for the last 8 years. Since i 'm about to adding another location, I want to revamp my letterhead and business card. I already have a logo i'm happy with. I will upload my current letterhead, fax sheet, envelope, and logos. I need a business card also. I have 2 locations, 1 phone number, 1 fax line, website, etc. If possible and fitting with the design, I would like to keep the same information listed currently on the letterhead.

**Keep in mind, I also NEED A FAX SHEET COVER. thank you
Updates

Hello, Please submit a Gray Scale or Black and White version of your designs also, since most of the time I will be printing NON color stationery. I will seldom use a color print for my letterhead, I would like to have a color version for my benefit, however i will print in grayscale majority of the time . For the Business Card, that can just be in color. When I get my business cards they will be in color.Thank youEnrique Added Sunday, September 18, 2016

Industry/Entity Type

Business

```html
<!DOCTYPE html>
<html lang="en">
<head>
<meta charset="utf-8">
<title>Marwick Law — Business Card</title>
<link rel="stylesheet" href="https://fonts.googleapis.com/css2?family=Source+Sans+3:wght@400;600&display=swap">
<style>
  :root {
    --page: #d8d1c8;
    --card: #eeebe7;
    --card-frost: #f7f5f2;
    --gold: #8d6c3a;
    --gold-light: #b9986a;
    --ink: #2b2a28;
    --ink-soft: #55524e;
    --black: #161616;
    --rule: #6f6a64;
  }
  * { margin: 0; padding: 0; box-sizing: border-box; }
  html, body { width: 1200px; height: 969px; overflow: hidden; }
  body {
    background: var(--page);
    font-family: "Source Sans 3", "Myriad Pro", Arial, sans-serif;
    position: relative;
  }
  .business-card {
    position: absolute;
    left: 100px; top: 201px;
    width: 1000px; height: 567px;
    background: var(--card);
    box-shadow: 0 10px 30px rgba(0,0,0,0.18);
    overflow: hidden;
  }
  .card-shapes { position: absolute; inset: 0; }
  .brand {
    position: absolute;
    left: 568px; top: 50px;
    width: 400px;
    text-align: center;
  }
  .brand-square {
    display: block;
    width: 78px; height: 78px;
    margin: 0 auto 34px;
    background: var(--gold);
  }
  .brand-name {
    font-size: 40px;
    font-weight: 600;
    letter-spacing: 2px;
    text-transform: uppercase;
    color: var(--gold);
    white-space: nowrap;
  }
  .person { position: absolute; left: 52px; top: 272px; }
  .person-name { font-size: 33px; font-weight: 600; color: var(--gold); line-height: 1.1; }
  .person-title { font-size: 25px; color: var(--ink); margin-top: 8px; }
  .contact-list {
    position: absolute; left: 52px; top: 378px;
    list-style: none;
  }
  .contact-item {
    display: flex; align-items: center;
    height: 38.5px;
    font-size: 25px; color: var(--ink-soft);
  }
  .contact-icon { width: 24px; height: 24px; margin-right: 20px; fill: var(--ink-soft); }
  .divider {
    position: absolute; left: 464px; top: 384px;
    width: 1.5px; height: 138px; background: var(--rule);
  }
  .office-list { position: absolute; left: 495px; top: 378px; }
  .office { font-size: 25px; color: var(--ink); line-height: 38.5px; }
</style>
</head>
<body>
  <main class="business-card">
    <svg class="card-shapes" viewBox="0 0 1000 567" width="1000" height="567" aria-hidden="true">
      <defs>
        <linearGradient id="goldFade" x1="0" y1="0" x2="1" y2="0.6">
          <stop offset="0" stop-color="var(--gold)"/>
          <stop offset="0.35" stop-color="#a88659"/>
          <stop offset="1" stop-color="#e4dbd0" stop-opacity="0"/>
        </linearGradient>
      </defs>
      <path d="M0 0 H560 V40 H0 Z" fill="url(#goldFade)"/>
      <path d="M0 0 H180 V220 H0 Z" fill="url(#goldFade)"/>
      <path d="M38 200 Q38 40 170 30 H1000 V567 H0 V200 Z" fill="var(--card-frost)"/>
      <path d="M1000 390 Q990 520 830 540 Q760 550 700 567 H1000 Z" fill="var(--black)"/>
    </svg>

    <div class="brand">
      <span class="brand-square"></span>
      <div class="brand-name">Marwick Law</div>
    </div>

    <div class="person">
      <h1 class="person-name">Tobias Marwick Esq.</h1>
      <p class="person-title">Attorney</p>
    </div>

    <ul class="contact-list">
      <li class="contact-item">
        <svg class="contact-icon" viewBox="0 0 24 24"><path d="M6.6 10.8a15 15 0 0 0 6.6 6.6l2.2-2.2a1 1 0 0 1 1-.25 11.4 11.4 0 0 0 3.6.57 1 1 0 0 1 1 1V20a1 1 0 0 1-1 1A17 17 0 0 1 3 4a1 1 0 0 1 1-1h3.5a1 1 0 0 1 1 1c0 1.25.2 2.45.57 3.6a1 1 0 0 1-.25 1z"/></svg>
        610.555.0142
      </li>
      <li class="contact-item">
        <svg class="contact-icon" viewBox="0 0 24 24"><path d="M7 1h10a2 2 0 0 1 2 2v18a2 2 0 0 1-2 2H7a2 2 0 0 1-2-2V3a2 2 0 0 1 2-2zm0 3v14h10V4zm5 15.5a1.2 1.2 0 1 0 0 2.4 1.2 1.2 0 0 0 0-2.4z"/></svg>
        484.555.0187
      </li>
      <li class="contact-item">
        <svg class="contact-icon" viewBox="0 0 24 24"><path d="M2 5h20v14H2zm2 2v.5l8 5 8-5V7zm0 2.8V17h16V9.8l-8 5z"/></svg>
        Tobias@MarwickLaw.com
      </li>
      <li class="contact-item">
        <svg class="contact-icon" viewBox="0 0 24 24"><path d="M12 2a10 10 0 1 0 0 20 10 10 0 0 0 0-20zm-1 17.9A8 8 0 0 1 4.2 10.6L9 15v1a2 2 0 0 0 2 2zm6.9-2.5A2 2 0 0 0 16 16h-1v-3a1 1 0 0 0-1-1H8v-2h2a1 1 0 0 0 1-1V7h2a2 2 0 0 0 2-2v-.4a8 8 0 0 1 2.9 12.8z"/></svg>
        www.MarwickLaw.com
      </li>
    </ul>

    <div class="divider"></div>

    <div class="office-list">
      <address class="office" style="font-style:normal">48 Harlow Ave.<br>Suite 200, Glenford, PA 19060</address>
      <address class="office" style="font-style:normal">710 Ashby St.<br>Kenton, PA 19015</address>
    </div>
  </main>
</body>
</html>
```